Venture Backed Startup Company for SaaS Lead Generation ***Guaranteed Payment and Fast Feedback***

***Guaranteed Payment***
***I Give Fast Feedback***

I need a one-page website design for a startup company. We sell lead generation and appointment setting services to B2B SaaS companies.

Looking for a clean, modern, flat, "Saas-style" design. A simple but trustworthy and authoritative color palette is best. Pictures of actual people are very good to use too

Here are some websites I like and the reasons why:

https://www.plimwerk.com - simple and intuitive design, very clear, strong CTA, explains the process succinctly, and has pics of people/faces\

https://www.tarnoseed.com/ - clean and simple, flat design, strong CTA, easy to understand

https://www.vurmtile.io/ - simple and clean navigation, easy to understand what to do next

https://quillbrashvantor.com/ - strong step by step approach, easy to understand the value of the website, clean and sharp design

https://pebrikloft.com/ - Great color scheme, clean, easy to read, great font

Target Market(s)

startups, entrepeneur, B2B SaaS

Industry/Entity Type

SaaS

Number of Pages Required

1 page

Font styles to use
Sans Serif

Colors

Designer to choose colors to be used in the design.

Requirements
Must have
• Good graphics, a theme, and pictures of people
Nice to have
• Here are other websites like and the reason why
• https://marzentilo.com/ - Great graphics, clean and flat design, pictures of people, modern design
• https://drovelunk.com/ - Clean, pictures of people, easy to read, good contrast
• https://pelkiwarn.co/ -- Good graphics and great font, easy to read, great color scheme
• http://fennicandwest.com/ - clean design

```html
<!DOCTYPE html>
<html lang="en">
<head>
<meta charset="utf-8">
<title>Vurmtile — Email Signature Generator</title>
<link href="https://fonts.googleapis.com/css2?family=Poppins:wght@400;500;600;700&family=Open+Sans:wght@400;600&display=swap" rel="stylesheet">
<style>
:root{
  --blue:#1f7fd0;
  --blue-deep:#155f9e;
  --blue-dark:#0f4f86;
  --blue-title:#1a73c2;
  --pink:#f36f92;
  --ink:#2a2a2a;
  --muted:#666;
  --light:#f2f4f7;
  --white:#fff;
  --dark-btn:#222;
}
*{margin:0;padding:0;box-sizing:border-box}
html,body{width:1200px;height:4534px;overflow:hidden}
body{position:relative;background:var(--white);font-family:"Open Sans",Arial,sans-serif;color:var(--ink)}
.abs{position:absolute}
h1,h2,h3,h4{font-family:"Poppins",Arial,sans-serif}
.center{text-align:center;left:0;width:1200px}

/* hero */
.hero{top:0;left:0;width:1200px;height:590px;overflow:hidden}
.hero-photo{position:absolute;inset:0;background:linear-gradient(120deg,#6d5ca8 0%,#5b74b8 40%,#7a9bd0 70%,#4e5f9c 100%)}
.hero-tint{position:absolute;inset:0;background:rgba(70,80,170,.45)}
.nav{top:40px;left:0;width:1200px;height:40px}
.brand{left:160px;top:10px;color:var(--white);font:600 14px "Poppins",sans-serif;letter-spacing:.5px}
.menu{left:584px;top:10px;display:flex;gap:30px}
.menu a{color:var(--white);font:600 13px "Poppins",sans-serif;text-decoration:none}
.signup{left:932px;top:0;width:108px;height:36px;border:1.5px solid var(--white);border-radius:3px;color:var(--white);font:600 13px "Poppins",sans-serif;display:flex;align-items:center;justify-content:center}
.hero h1{top:204px;color:var(--white);font-size:36px;line-height:40px;font-weight:700}
.hero-sub{top:290px;color:var(--white);font-size:16px;line-height:24px}
.btn-pink{background:var(--pink);color:var(--white);font:600 12px "Poppins",sans-serif;display:flex;align-items:center;justify-content:center;border-radius:3px}
.hero .btn-pink{left:548px;top:362px;width:104px;height:36px}

.section-title{font-size:30px;font-weight:600;color:var(--blue-title)}
.section-sub{font-size:14px;color:var(--ink)}

/* features */
.swirl{top:880px;left:0;width:1200px;height:560px;background:radial-gradient(ellipse at 40% 40%,#e9f4fc 0%,#b8dbf3 30%,#6fb2e6 50%,#dcecf8 70%,#fff 90%)}
.person-photo{left:240px;top:700px;width:276px;height:540px;background:linear-gradient(180deg,#f4f4f4 0%,#c9c9cf 50%,#3a3d4d 100%);border-radius:4px}
.timeline{left:612px;top:760px;width:2px;height:400px;border-left:2px dashed var(--blue)}
.feature{left:594px;width:480px;height:80px}
.feature .ic{position:absolute;left:0;top:0;width:38px;height:38px;border-radius:50%;background:var(--white);border:2px solid var(--blue);display:flex;align-items:center;justify-content:center}
.feature h3{position:absolute;left:80px;top:0;font-size:18px;font-weight:500;color:var(--blue-title)}
.feature p{position:absolute;left:80px;top:28px;width:310px;font-size:11px;line-height:15px;color:#444}
.about h2{top:1322px;font-size:30px;font-weight:600;color:var(--blue-title)}
.about p{top:1378px;left:210px;width:780px;text-align:center;font-size:16px;line-height:24px;color:#222}

/* help cards */
.help-card{top:1795px;width:420px;height:245px;border-radius:4px;color:var(--white);padding:118px 38px 0}
.help-card h3{font-size:22px;font-weight:500;margin-bottom:10px}
.help-card p{font-size:12px;line-height:16px}
.card-blue{left:166px;background:linear-gradient(135deg,#2d8fe0,#1b6fc0)}
.card-pink{left:601px;background:linear-gradient(135deg,#f58aa5,#e46a8a)}
.band-mid{top:1980px;left:0}
.band-mid h2{top:2105px;color:var(--white);font-size:30px;font-weight:500}
.btn-outline{left:423px;top:2165px;width:350px;height:55px;background:var(--white);border-radius:4px;color:#f08a2a;font:500 17px "Poppins",sans-serif;display:flex;align-items:center;justify-content:center}

/* hands */
.hands-title{top:2395px;font-size:30px;font-weight:500;color:#222}
.hand-card{top:2470px;width:258px;height:260px;text-align:center;padding-top:28px}
.hand-card.mid{top:2460px;width:280px;height:275px;background:var(--white);border-radius:0 30px 0 30px;box-shadow:0 4px 22px rgba(0,0,0,.15)}
.hand-card svg{display:block;margin:0 auto 14px}
.hand-card h4{font-size:16px;font-weight:600;color:#111;margin-bottom:10px}
.hand-card p{font-size:10px;line-height:14px;color:#555;width:190px;margin:0 auto 14px}
.read-more{display:inline-block;background:#e4e4e4;color:#333;font:600 10px "Poppins",sans-serif;padding:8px 20px}

/* seo */
.seo{top:2785px;left:0;width:1200px;height:265px;background:linear-gradient(90deg,#1f5b90,#2a6fab 50%,#1f5b90)}
.seo h2{top:2855px;color:var(--white);font-size:26px;font-weight:600;letter-spacing:1px}
.seo-sub{top:2892px;color:var(--white);font-size:16px}
.field{top:2935px;height:46px;background:var(--white);display:flex;align-items:center;justify-content:space-between;padding:0 16px;font-size:13px;color:#444}
.seo .btn-pink{left:795px;top:2935px;width:150px;height:46px;font-size:15px;border-radius:0}

/* pricing */
.pricing-bg{top:3050px;left:0;width:1200px;height:290px;background:var(--blue)}
.pricing-title{top:3100px;color:var(--white);font-size:26px;font-weight:600;letter-spacing:1px}
.pricing-sub{top:3138px;color:var(--white);font-size:14px;font-weight:600}
.plan{top:3220px;width:272px;height:445px;background:var(--white);box-shadow:0 2px 14px rgba(0,0,0,.12);text-align:center}
.plan-head{height:165px;background:#c4c4c4;color:var(--white);padding-top:38px}
.plan-name{font-size:12px}
.price{font:600 46px "Poppins",sans-serif;line-height:56px}
.price sup{font-size:20px;vertical-align:22px;margin-right:2px}
.per{font-size:9px}
.plan ul{list-style:none;padding-top:28px;font-size:14px;color:#555;line-height:34px}
.plan .btn{display:inline-block;margin-top:20px;width:110px;height:38px;line-height:38px;background:var(--dark-btn);color:var(--white);font:600 11px "Poppins",sans-serif}
.plan.featured{top:3200px;width:310px;height:520px;z-index:2}
.plan.featured .plan-head{background:var(--pink);height:210px;padding-top:58px}
.plan.featured .btn{background:var(--pink)}

/* testimonial */
.bottom-band{top:3940px;left:0;width:1200px;height:594px;background:linear-gradient(180deg,#2c8ee0,#2278c8)}
.testimonial{top:3760px;left:180px;width:836px;height:350px;background:var(--white);border-radius:0 0 40px 0;box-shadow:0 4px 20px rgba(0,0,0,.15);z-index:3}
.avatar{position:absolute;left:92px;top:-40px;width:170px;height:170px;border-radius:50%;background:radial-gradient(circle at 50% 40%,#e8c9b4,#8a5a44 70%);border:4px solid var(--white)}
.t-name{position:absolute;left:60px;top:140px;width:236px;text-align:center;font:500 18px "Poppins",sans-serif;color:#222}
.t-role{position:absolute;left:60px;top:168px;width:236px;text-align:center;font-size:12px;color:#444}
.dots{position:absolute;left:120px;top:205px;display:flex;gap:8px}
.dots span{width:34px;height:12px;border-radius:6px;background:#ddd}
.dots span:first-child{background:#333}
.t-head{position:absolute;left:350px;top:42px;font:700 20px "Poppins",sans-serif;color:#111}
.t-text{position:absolute;left:350px;top:76px;width:420px;font-size:13px;line-height:18px;color:#555}
.quote{position:absolute;font:700 70px "Poppins",sans-serif;color:#ccc;line-height:1}

/* footer */
.news-title{top:4170px;color:var(--white);font:600 12px "Poppins",sans-serif;letter-spacing:1px}
.news-input{left:408px;top:4218px;width:248px;height:40px;background:#cfe3f5}
.news-btn{left:656px;top:4218px;width:135px;height:40px;background:var(--white);color:#333;font-size:14px;display:flex;align-items:center;justify-content:center}
.contact{top:4312px;display:flex;gap:12px;color:var(--white)}
.contact h5{font:600 13px "Poppins",sans-serif;margin-bottom:4px}
.contact p{font-size:11px;line-height:15px}
.copyright{top:4450px;color:var(--white);font-size:12px}
</style>
</head>
<body>

<header class="abs hero">
  <div class="hero-photo" role="img" aria-label="Photo of business people shaking hands at a desk"></div>
  <div class="hero-tint"></div>
  <nav class="abs nav">
    <div class="abs brand">VURMTILE</div>
    <div class="abs menu"><a>FEATURES</a><a>TESTIMONIALS</a><a>PRICING</a><a>LOGIN</a></div>
    <div class="abs signup">SIGN UP</div>
  </nav>
  <h1 class="abs center">Use a Business Email Signature Generator<br>Reveal a New Marketing Channel</h1>
  <p class="abs center hero-sub">Create professional email signatures for your team Stay true to<br>your brand identity, run banner campaigns</p>
  <div class="abs btn-pink">TRY NOW</div>
  <svg class="abs" style="left:0;top:470px" width="1200" height="120" viewBox="0 0 1200 120" preserveAspectRatio="none">
    <path d="M0 40 C300 110 800 110 1200 10 L1200 120 L0 120Z" fill="#2d6fc6" opacity=".8"/>
    <path d="M0 60 C320 120 820 110 1200 40 L1200 120 L0 120Z" fill="#fff"/>
  </svg>
</header>

<div class="abs swirl" role="img" aria-label="Flowing blue abstract ribbon graphic"></div>
<h2 class="abs center section-title" style="top:622px">We corporate email signature generator</h2>
<p class="abs center section-sub" style="top:668px">is the most compelling and straightforward solution for signature marketing.</p>
<div class="abs person-photo" role="img" aria-label="Photo of a businessman in a suit jumping with joy"></div>
<div class="abs timeline"></div>
<div class="abs feature" style="top:760px"><div class="ic"><svg width="18" height="18"><circle cx="9" cy="7" r="4" fill="none" stroke="#1f7fd0" stroke-width="2"/><path d="M2 17c1-4 13-4 14 0" fill="none" stroke="#1f7fd0" stroke-width="2"/></svg></div><h3>Create Group</h3><p>You can create groups as per the interest of your sharing information to people</p></div>
<div class="abs feature" style="top:845px"><div class="ic"><svg width="18" height="18"><path d="M3 4h12M3 9h12M3 14h12" stroke="#1f7fd0" stroke-width="2"/></svg></div><h3>Show Group List</h3><p>Group list is also visible to set up group calling for specific purpose</p></div>
<div class="abs feature" style="top:930px"><div class="ic"><svg width="18" height="18"><path d="M9 3v12M3 9h12" stroke="#1f7fd0" stroke-width="2"/></svg></div><h3>Add People to Group</h3><p>Users are allowed to add multiple contacts from their phone contact list</p></div>
<div class="abs feature" style="top:1015px"><div class="ic"><svg width="18" height="18"><path d="M3 15l2-5 8-8 3 3-8 8z" fill="none" stroke="#1f7fd0" stroke-width="2"/></svg></div><h3>Manual Entry of People</h3><p>Contacts can also be added manually. User needs to fill form and other associated data</p></div>
<div class="abs feature" style="top:1100px"><div class="ic"><svg width="18" height="18"><path d="M4 5h10M6 5v10h6V5M8 3h2" fill="none" stroke="#1f7fd0" stroke-width="2"/></svg></div><h3>Delete Individual History</h3><p>A user is allowed to delete the history individually</p></div>

<section class="about">
  <h2 class="abs center">About us</h2>
  <p class="abs">Lorem Ipsum is simply dummy text of the printing and typesetting industry. Lorem Ipsum has been the industry's standard dummy text ever since the 1500s, when an unknown printer took a galley of type and scrambled it to make a type specimen book. It has survived not only five centuries, but also the leap into electronic typesetting, remaining essentially unchanged.</p>
</section>

<h2 class="abs center section-title" style="top:1692px">What can Vurmtile help you achieve?</h2>
<p class="abs center section-sub" style="top:1738px">is the most compelling and straightforward solution for signature marketing.</p>
<svg class="abs band-mid" width="1200" height="370" viewBox="0 0 1200 370" preserveAspectRatio="none"><path d="M0 60 L1200 0 L1200 370 L0 370Z" fill="#175f9c"/></svg>
<div class="abs help-card card-blue" role="img" aria-label="Blue tinted photo of a person at a laptop"><h3>Get Full Profile Information</h3><p>Search for prospects, get full profile information with verified email address and mutual contacts</p></div>
<div class="abs help-card card-pink" role="img" aria-label="Pink tinted photo of a world map on a screen"><h3>Unlock Team Network</h3><p>Search for prospects, get full profile information with verified email address and mutual contacts</p></div>
<h2 class="abs center" style="top:2105px;color:#fff;font-size:30px;font-weight:500">Want to know how it works?</h2>
<div class="abs btn-outline">Request Product Presentation</div>

<h2 class="abs center hands-title">You and your team are in good hands</h2>
<div class="abs hand-card" style="left:188px">
  <svg width="60" height="52"><rect x="6" y="6" width="48" height="32" fill="none" stroke="#222" stroke-width="2"/><path d="M22 46h16M30 38v8" stroke="#222" stroke-width="2"/><path d="M14 28l10-10 8 6 12-12" fill="none" stroke="#222" stroke-width="2"/></svg>
  <h4>DIGITAL MARKETING</h4><p>Curabitur quam felis tortor lacus iaculis ullamcorper magna nisl vitae sodales facilisis augue tempor eros</p><span class="read-more">READ MORE</span></div>
<div class="abs hand-card mid" style="left:462px">
  <svg width="60" height="52"><circle cx="30" cy="26" r="20" fill="none" stroke="#222" stroke-width="2"/><path d="M10 26h40M30 6c-10 12-10 28 0 40M30 6c10 12 10 28 0 40" fill="none" stroke="#222" stroke-width="2"/></svg>
  <h4>BUSINESS INCUBATOR</h4><p>Curabitur quam felis tortor lacus iaculis ullamcorper magna nisl vitae sodales facilisis augue tempor eros</p><span class="read-more">READ MORE</span></div>
<div class="abs hand-card" style="left:755px">
  <svg width="60" height="52"><rect x="8" y="4" width="44" height="34" fill="none" stroke="#222" stroke-width="2"/><circle cx="30" cy="17" r="6" fill="none" stroke="#222" stroke-width="2"/><path d="M20 34c2-8 18-8 20 0M20 46h20M30 38v8" fill="none" stroke="#222" stroke-width="2"/></svg>
  <h4>BUSINESS APPLICATION</h4><p>Curabitur quam felis tortor lacus iaculis ullamcorper magna nisl vitae sodales facilisis augue tempor eros</p><span class="read-more">READ MORE</span></div>

<section class="abs seo" role="img" aria-label="Faint pattern of office icons on blue"></section>
<h2 class="abs center seo" style="background:none;height:auto;top:2855px">GET FREE WEBSITE SEO SCORE ONLINE</h2>
<p class="abs center seo-sub">Enter your email to get the same chearsheet for SEO</p>
<div class="abs field" style="left:257px;width:268px"><span>Enter your website URL</span><svg width="16" height="16"><circle cx="8" cy="8" r="6" fill="none" stroke="#666" stroke-width="1.5"/><path d="M2 8h12M8 2v12" stroke="#666"/></svg></div>
<div class="abs field" style="left:526px;width:269px"><span>Enter your Email</span><svg width="18" height="14"><rect x="1" y="1" width="16" height="12" fill="none" stroke="#666" stroke-width="1.5"/><path d="M1 1l8 7 8-7" fill="none" stroke="#666" stroke-width="1.5"/></svg></div>
<div class="abs btn-pink" style="left:795px;top:2935px;width:150px;height:46px;font-size:15px;border-radius:0">SUBMIT NOW</div>

<div class="abs pricing-bg"></div>
<h2 class="abs center pricing-title">OUR PRICING</h2>
<p class="abs center pricing-sub">Choose the plan that best fits your needs</p>
<div class="abs plan" style="left:176px">
  <div class="plan-head"><div class="plan-name">Standard</div><div class="price"><sup>$</sup>49</div><div class="per">MONTHLY</div></div>
  <ul><li>5 Projects</li><li>5 GB Storage</li><li>Unlimited Users</li><li>10 GB Bandwith</li><li>Fully SEO Features</li></ul><span class="btn">SELECT PLAN</span></div>
<div class="abs plan featured" style="left:446px">
  <div class="plan-head"><div class="plan-name">Premium</div><div class="price"><sup>$</sup>79</div><div class="per">MONTHLY</div></div>
  <ul><li>5 Projects</li><li>5 GB Storage</li><li>Unlimited Users</li><li>10 GB Bandwith</li><li>5 Inner Pages</li><li>Fully SEO Features</li></ul><span class="btn">SELECT PLAN</span></div>
<div class="abs plan" style="left:750px">
  <div class="plan-head"><div class="plan-name">Professional</div><div class="price"><sup>$</sup>199</div><div class="per">MONTHLY</div></div>
  <ul><li>5 Projects</li><li>5 GB Storage</li><li>Unlimited Users</li><li>10 GB Bandwith</li><li>Fully SEO Features</li></ul><span class="btn">SELECT PLAN</span></div>

<div class="abs bottom-band" role="img" aria-label="Blue tinted photo of people working at laptops"></div>
<section class="abs testimonial">
  <div class="avatar" role="img" aria-label="Portrait photo of the customer"></div>
  <div class="t-name">Marla Fenwick</div>
  <div class="t-role">CEO Girl Lorem</div>
  <div class="dots"><span></span><span></span><span></span></div>
  <span class="quote" style="left:290px;top:28px">“</span>
  <h3 class="t-head">WHAT OUR CUSTOMERS SAYS</h3>
  <p class="t-text">Quae voluptatibus suscipit debitis, ad minus dolor sit amet. Qui iure voluptatem ratione sint, corrupti a ex adipisci et deleniti debitis. Repellendus, eos aliquid recusandae id suscipit quis labore nesciunt.</p>
  <span class="quote" style="left:720px;top:150px">”</span>
</section>

<p class="abs center news-title">SUBSCRIBE TO OUR NEWSLETTER</p>
<div class="abs news-input"></div>
<div class="abs news-btn">Subscribe</div>
<div class="abs contact" style="left:268px"><svg width="20" height="26"><path d="M10 25C4 16 2 12 2 9a8 8 0 0116 0c0 3-2 7-8 16z" fill="#fff"/><circle cx="10" cy="9" r="3" fill="#2278c8"/></svg><div><h5>Address Information</h5><p>88 Tessen Row, Harlow Bay,<br>NY 10987</p></div></div>
<div class="abs contact" style="left:552px"><svg width="26" height="20"><rect x="1" y="2" width="24" height="16" fill="none" stroke="#fff" stroke-width="2"/><path d="M1 2l12 9 12-9" fill="none" stroke="#fff" stroke-width="2"/></svg><div><h5>Email Address</h5><p>hello@vurmtile.io</p></div></div>
<div class="abs contact" style="left:790px"><svg width="22" height="22"><path d="M4 2l5 1 1 5-3 2c1 3 3 5 6 6l2-3 5 1 0 5c-10 1-18-7-17-17z" fill="#fff"/></svg><div><h5>Contact Us</h5><p>+000 0000 0000</p></div></div>
<p class="abs center copyright">© 2018 website · All rights reserved</p>

</body>
</html>
```